Medical centre needs a business card

We are a medcial centre in Australia, needing a new business card. Our demographic is low working class families. We are going to be renovating our premises to modernise the look and also had a new logo done a few months ago representing quality and community, and now need to update our cards. It needs to be doubled sided, with logo and contact details on the front, and appointment details on the back. . Needs to be modern and simple, easy to read. <br/><br/>Name: Kindle Grove Medical Centre <br/>Address: 512 Larkin Rd (Cnr Larkin Rd & Fenwick Vale Rd),<br/>Tamsworth Court Shopping Centre, Paralowie, SA 5108<br/>Ph: 08 8193 4067<br/>Tag line: Where your care comes first<br/>Website: www.kindlegrovemedicalexample.com.au<br/>Online bookings also available<br/><br/>(On the back, to have 3 lines of appointments that can be written in.<br/>Day, date, time)<br/><br/>Your next appointment is on<br/>Can try “M T W Th F Sa Su _________________ at ____________ am/pm” or other combinations <br/>Please advise as soon as possible if unable to attend<br/>Cancellation fees apply if less than 2 hrs notice<br/>Online appointments available (please highlight this option by either by position, colour or font)

Target Market(s)

Lower social economic working class, young families to seniors

Industry/Entity Type

Medical Centre

Contact Information for Business Card

Kindle Grove Medical Centre
512 Larkin Rd (Cnr Larkin Rd & Fenwick Vale Drive)
Tamsworth Court Shopping Centre
Paralowie SA 5108
Ph: 08 8193 4067
www.kindlegrovemedicalexample.com.au
Tagline line: where your care comes first
Back side is for appointments
Your next appointment is with Dr ______________
Day/date/time (Please give 3 lines of appointments)
Please advise as soon as possible if unable to attend
Cancellation fees apply if less than 2 hours notice
Online appointments available
Book online easily and conveniently (please highlight online appointments)

Font styles to use
Serif
Sans Serif

Colors

Designer to choose colors to be used in the design.

Requirements
Must have
• Modern and simple
• Easy to ready
• Induces a wellbeing feeling
• Incorporate our logo colours and feel from logo
• Induces feeling of stability and security
Nice to have
• Attract attention
• Pleasant to look at
• Feeling of innovation
Should not have
• Loud clashing colours
• Overly luxurious feeling
• Overly artistic

```html
<!DOCTYPE html>
<html lang="en">
<head>
<meta charset="utf-8">
<title>Appointment Card – Back</title>
<link rel="stylesheet" href="https://fonts.googleapis.com/css2?family=Quicksand:wght@300;400;700&display=swap">
<style>
  :root {
    --ink-blue: #1b76bc;
    --paper: #ffffff;
  }
  html, body {
    margin: 0;
    padding: 0;
    width: 1200px;
    height: 699px;
    overflow: hidden;
    background: var(--paper);
  }
  .card-back {
    position: relative;
    width: 1200px;
    height: 699px;
    background: var(--paper);
    color: var(--ink-blue);
    font-family: "Quicksand", sans-serif;
    font-weight: 300;
  }
  .field-row {
    position: absolute;
    left: 171px;
    display: flex;
    align-items: flex-end;
    white-space: nowrap;
  }
  .field-label {
    margin: 0;
    font-size: 38px;
    line-height: 1;
    letter-spacing: -1.4px;
  }
  .write-line {
    flex: none;
    width: 308px;
    height: 0;
    border-top: 2.5px solid var(--ink-blue);
    margin-bottom: 4px;
  }
  .doctor-row { top: 138px; }
  .doctor-row .write-line { margin-left: 24px; }

  .short-row .field-label { width: 108px; letter-spacing: -0.6px; }
  .day-row  { top: 194px; }
  .date-row { top: 250px; }
  .time-row { top: 306px; }

  .notice-list {
    position: absolute;
    left: 171px;
    top: 392px;
    margin: 0;
    padding: 0;
    list-style: none;
    font-size: 29.5px;
    line-height: 39px;
    letter-spacing: 0;
    white-space: nowrap;
  }
  .notice-list .highlight {
    font-weight: 700;
    letter-spacing: 0.3px;
  }
</style>
</head>
<body>
  <main class="card-back">
    <div class="field-row doctor-row">
      <p class="field-label">Your next appointment is with Dr</p>
      <div class="write-line"></div>
    </div>

    <div class="field-row short-row day-row">
      <p class="field-label">Day</p>
      <div class="write-line"></div>
    </div>

    <div class="field-row short-row date-row">
      <p class="field-label">Date</p>
      <div class="write-line"></div>
    </div>

    <div class="field-row short-row time-row">
      <p class="field-label">Time</p>
      <div class="write-line"></div>
    </div>

    <ul class="notice-list">
      <li>Please advise as soon as possible if unable to attend</li>
      <li>Cancellation fees apply if less than 2 hours notice</li>
      <li class="highlight">Online appointments available</li>
      <li>Book online easily and conveniently</li>
    </ul>
  </main>
</body>
</html>
```